Bright Harbour Mortgages Social Media Campaign

I need social media campaign banners. Facebook and Instagram.
I would like them to incorporate local photos, my photo and my logo. I have some sample files of previous campaigns and I have a color scheme associated with my brand. My business operates in St. John's Newfoundland.

Target Market(s)

Home Buyers, Home Owners

Industry/Entity Type

Mortgage Brokering

Logo Text

Bright Harbour Mortgages

Logo styles of interest
Lettermark Logo
Font styles to use
Other font styles liked:
• Times New Roman, I'm open to suggestion

Colors
0054AA
0677BA
7BADD7
CADEEF
E8F1F8
EE7325
F08F49
F5BC92
FAE3D3
FDF4ED

Requirements
Must have
• My name, photo, contact info, slogan
Nice to have
• We can discuss slogans to use, I can provide some suggestions.

```html
<!DOCTYPE html>
<html lang="en">
<head>
<meta charset="UTF-8">
<title>Bright Harbour Mortgages – Social Banner</title>
<link href="https://fonts.googleapis.com/css2?family=Roboto:ital,wght@0,300;0,400;0,700;0,900;1,900&display=swap" rel="stylesheet">
<style>
  :root {
    --navy: #0c1f5a;
    --orange: #fc4f0e;
    --sky-light: #dbe8ef;
    --sky-mid: #b7d1df;
    --sky-deep: #7fb0c9;
    --band: #e4edf3;
    --band-alt: #d3e2ec;
    --white: #ffffff;
  }
  * { margin: 0; padding: 0; box-sizing: border-box; }
  html, body { width: 1200px; height: 1200px; overflow: hidden; }
  body { font-family: "Roboto", Arial, sans-serif; background: var(--sky-light); }

  .banner { position: relative; width: 1200px; height: 1200px; overflow: hidden; }

  .scene-photo {
    position: absolute; inset: 0;
    background:
      radial-gradient(ellipse 520px 600px at 930px 430px, #e9eef2 0%, #c9d6de 55%, transparent 75%),
      radial-gradient(ellipse 300px 220px at 290px 950px, #d6dfe5 0%, transparent 70%),
      linear-gradient(180deg, #dce9f0 0%, #c6dbe6 45%, #9fc3d6 100%);
  }

  .agent-photo {
    position: absolute; left: 705px; top: 480px; width: 495px; height: 660px;
    border-radius: 240px 240px 0 0;
    background: linear-gradient(180deg, #d9a06f 0%, #e8c2a3 35%, #1e2c4f 70%, #17223f 100%);
  }

  .brand { position: absolute; left: 78px; top: 112px; display: flex; align-items: center; gap: 18px; }
  .brand-square { width: 40px; height: 40px; background: var(--orange); }
  .brand-name { font-size: 44px; font-weight: 700; color: var(--orange); letter-spacing: 0.5px; }

  .slogan {
    position: absolute; left: 312px; top: 170px; width: 556px;
    display: flex; align-items: center; gap: 14px;
    font-size: 19px; font-weight: 700; color: var(--navy); letter-spacing: 3px; white-space: nowrap;
  }
  .slogan::before, .slogan::after { content: ""; flex: 1; height: 3px; background: var(--navy); }

  .headline {
    position: absolute; left: 70px; top: 262px;
    font-size: 56px; font-weight: 900; line-height: 66px; color: var(--navy); letter-spacing: -0.5px;
  }
  .headline .accent { color: var(--orange); font-style: italic; }
  .headline .brand-line { font-size: 50px; }

  .offer { position: absolute; left: 70px; top: 500px; color: var(--navy); }
  .offer-lead, .offer-tail { font-size: 29px; font-weight: 300; line-height: 40px; }
  .offer-key { font-size: 37px; font-weight: 700; color: var(--orange); line-height: 46px; }

  .cta {
    position: absolute; left: 70px; top: 686px; width: 255px; height: 58px;
    background: var(--navy); color: var(--white);
    font-size: 30px; font-weight: 700; letter-spacing: 0.3px;
    display: flex; align-items: center; justify-content: center;
    clip-path: polygon(10px 0, calc(100% - 10px) 0, 100% 10px, 100% calc(100% - 10px), calc(100% - 10px) 100%, 10px 100%, 0 calc(100% - 10px), 0 10px);
  }

  .contact-band {
    position: absolute; left: 0; top: 1140px; width: 1200px; height: 60px;
    display: flex; background: var(--band);
  }
  .contact-item {
    display: flex; align-items: center; gap: 12px;
    font-size: 28px; font-weight: 700; color: var(--navy);
  }
  .contact-phone { width: 703px; padding-left: 72px; }
  .contact-web { flex: 1; padding-left: 14px; background: var(--band-alt); }
  .contact-item svg { width: 30px; height: 30px; flex: none; }
</style>
</head>
<body>
  <div class="banner">
    <div class="scene-photo" role="img" aria-label="Photo of a model house on stacked banknotes with house keys on a keyring on a pale blue surface"></div>
    <div class="agent-photo" role="img" aria-label="Portrait photo of the mortgage broker Maren, smiling, in a navy top"></div>

    <div class="brand">
      <span class="brand-square"></span>
      <span class="brand-name">BRIGHT HARBOUR MORTGAGES</span>
    </div>
    <div class="slogan">WE THINK OUTSIDE THE BOX</div>

    <h1 class="headline">
      Get The Keys To Your<br>
      <span class="accent">DREAM HOME</span> With<br>
      <span class="accent brand-line">BRIGHT HARBOUR MORTGAGES!</span>
    </h1>

    <div class="offer">
      <p class="offer-lead">Let Us Help You Unlock Your</p>
      <p class="offer-key">DREAM HOME TODAY</p>
      <p class="offer-tail">With Low Rates &amp; Great Deals!</p>
    </div>

    <div class="cta">GET STARTED</div>

    <div class="contact-band">
      <div class="contact-item contact-phone">
        <svg viewBox="0 0 24 24" aria-hidden="true" fill="none" stroke="#0c1f5a" stroke-width="2" stroke-linecap="round" stroke-linejoin="round">
          <path d="M6.6 2.8l2.5 0.2 1.4 4-1.8 1.6a12 12 0 0 0 6.7 6.7l1.6-1.8 4 1.4 0.2 2.5a3 3 0 0 1-3.2 2.8A17 17 0 0 1 3.8 6a3 3 0 0 1 2.8-3.2z" fill="#0c1f5a"/>
          <path d="M15 3.5a6 6 0 0 1 5.5 5.5M15 7a2.5 2.5 0 0 1 2 2"/>
        </svg>
        <span>CALL Maren: 709-555-0142</span>
      </div>
      <div class="contact-item contact-web">
        <svg viewBox="0 0 24 24" aria-hidden="true" fill="none" stroke="#0c1f5a" stroke-width="2">
          <circle cx="12" cy="12" r="10" fill="#0c1f5a"/>
          <ellipse cx="12" cy="12" rx="4" ry="10" stroke="#e4edf3" stroke-width="1.5"/>
          <path d="M2 12h20M4 7h16M4 17h16" stroke="#e4edf3" stroke-width="1.5"/>
        </svg>
        <span>www.harbourlinehomes.com</span>
      </div>
    </div>
  </div>
</body>
</html>
```